MOLVT Study flyer

I need help designing a flyer for a research study that will include brain imaging in adolescents. The info is in the attached document. The study is called the Marrowby Orchard Lantern Vesper Trail (MOLVT) study. Ideally this would be returned as a document that I can edit in the future as we will have several new recruitment phases (different age groups, etc. I also would love to have a logo designed as part of this project, but I recognize that might be a separate design request.

```html
<!DOCTYPE html>
<html lang="en">
<head>
<meta charset="utf-8">
<title>MOLVT Study Flyer</title>
<link href="https://fonts.googleapis.com/css2?family=Poppins:wght@700;800&family=Roboto:wght@400;500;700&family=Dancing+Script:wght@700&display=swap" rel="stylesheet">
<style>
  :root {
    --navy: #233d63;
    --gold: #dba12f;
    --copper: #c47a3a;
    --page: #eef2f8;
    --card: #ffffff;
    --ink: #2b2b2b;
    --white: #ffffff;
  }
  * { box-sizing: border-box; margin: 0; padding: 0; }
  html, body { width: 927px; height: 1200px; overflow: hidden; }
  body { font-family: "Roboto", sans-serif; color: var(--ink); }
  .flyer {
    position: relative; width: 927px; height: 1200px; overflow: hidden;
    background: linear-gradient(180deg, #f7f9fc 0%, var(--page) 60%, #e9eef6 100%);
  }
  .tag {
    position: absolute; left: 0; top: 0; width: 334px; height: 86px;
    background: var(--navy); border-radius: 0 0 43px 0; border-top-right-radius: 43px;
    color: var(--white); font-family: "Poppins", sans-serif; font-weight: 700;
    font-size: 29px; letter-spacing: 0.5px; display: flex; align-items: center; padding-left: 27px;
  }
  .title-acronym {
    position: absolute; left: 57px; top: 92px; font-family: "Poppins", sans-serif;
    font-weight: 800; font-size: 62px; color: var(--navy); letter-spacing: 1px;
  }
  .title-script {
    position: absolute; left: 55px; top: 138px; font-family: "Dancing Script", cursive;
    font-weight: 700; font-size: 118px; color: var(--gold); line-height: 1;
  }
  .hero-question {
    position: absolute; left: 57px; top: 296px; font-size: 22px; line-height: 30px; color: #2f2f2f;
  }
  .hero-sub {
    position: absolute; left: 57px; top: 363px; font-size: 16px; color: #333;
  }
  .hero-photo {
    position: absolute; left: 398px; top: -16px; width: 514px; height: 514px; border-radius: 50%;
    background: radial-gradient(circle at 55% 70%, #3a3a3d 0%, #6d6d70 30%, #c9c9cb 60%, #e4e4e6 100%);
    clip-path: inset(0 0 98px 0);
  }
  .intro-band {
    position: absolute; left: 56px; top: 400px; width: 871px; height: 169px;
    background: var(--copper); border-radius: 85px 0 0 85px;
  }
  .intro-icon {
    position: absolute; left: 30px; top: 25px; width: 119px; height: 119px; border-radius: 50%;
    background: var(--white); display: flex; align-items: center; justify-content: center;
  }
  .intro-text {
    position: absolute; left: 177px; top: 33px; width: 640px; color: var(--white);
    font-size: 19px; line-height: 30px;
  }
  .card {
    position: absolute; top: 591px; width: 391px; height: 534px; background: var(--card);
    border-radius: 22px; box-shadow: 0 4px 18px rgba(35,61,99,0.08); overflow: hidden;
  }
  .card-left { left: 60px; }
  .card-right { left: 474px; }
  .card-heading {
    position: absolute; left: 51px; top: 40px; font-family: "Poppins", sans-serif; font-weight: 800;
    font-size: 26px; line-height: 33px; color: var(--navy);
  }
  .brain-sketch {
    position: absolute; left: 271px; top: 10px; width: 118px; height: 116px; border-radius: 50%;
    background: radial-gradient(circle, #f1f1f1 0%, #fafafa 70%, transparent 100%);
  }
  .step { position: absolute; left: 52px; display: flex; gap: 20px; }
  .step-icon {
    width: 63px; height: 63px; border-radius: 50%; flex: none;
    display: flex; align-items: center; justify-content: center;
  }
  .step-icon.copper { background: var(--copper); }
  .step-icon.navy { background: var(--navy); }
  .step-text { font-size: 15.5px; line-height: 22px; color: #333; width: 220px; }
  .criteria { position: absolute; left: 51px; display: flex; gap: 14px; }
  .criteria svg { flex: none; margin-top: 2px; }
  .criteria p { font-size: 15.5px; line-height: 22px; color: #333; width: 260px; }
  .child-photo {
    position: absolute; left: 0; top: 312px; width: 391px; height: 222px;
    background: linear-gradient(110deg, #ffffff 0%, #eaf1fb 40%, #b9cdea 62%, #3e3a3c 80%, #1f2535 100%);
  }
  .compensation {
    position: absolute; left: 0; top: 440px; width: 220px; height: 94px; background: var(--copper);
    border-radius: 0 60px 0 0; color: var(--white); padding: 16px 0 0 39px;
  }
  .compensation .label { font-size: 20px; font-weight: 500; }
  .compensation .amount { font-size: 20px; font-weight: 500; margin-top: 2px; }
  .compensation .amount strong { font-size: 29px; font-weight: 700; }
  .footer {
    position: absolute; left: 0; top: 1152px; width: 927px; height: 48px; background: var(--navy);
    border-top-right-radius: 60px; color: var(--white); font-weight: 700; font-size: 16.5px;
  }
  .footer .cta { position: absolute; left: 35px; top: 13px; }
  .footer .cta a { color: var(--gold); text-decoration: underline; }
  .footer .email { position: absolute; left: 668px; top: 13px; display: flex; gap: 10px; align-items: center; font-size: 15px; }
  .footer .code { position: absolute; left: 894px; top: 19px; font-size: 8px; font-weight: 400; }
</style>
</head>
<body>
<div class="flyer">
  <div class="tag">RESEARCH STUDY</div>
  <div class="title-acronym">MOLVT</div>
  <div class="title-script">Study</div>
  <p class="hero-question">Are you the parent of a<br>child age 10-17?</p>
  <p class="hero-sub">Do they worry or overthink negative emotions?</p>

  <div class="hero-photo" role="img" aria-label="Photo of a teenage girl looking down, with scribbled question marks and symbols swirling above her head"></div>

  <div class="intro-band">
    <div class="intro-icon">
      <svg width="60" height="60" viewBox="0 0 60 60" fill="none" stroke="#c47a3a" stroke-width="2.2" stroke-linecap="round">
        <path d="M29 8c-5-4-13-2-14 4-6 0-9 6-6 11-4 3-4 10 1 12-2 6 3 11 9 10 1 5 7 8 10 4z"/>
        <path d="M31 8c5-4 13-2 14 4 6 0 9 6 6 11 4 3 4 10-1 12 2 6-3 11-9 10-1 5-7 8-10 4z"/>
        <path d="M30 8v41M18 20c4 0 6 2 6 5M14 32c4 0 7-2 8-5M22 42c0-4 3-6 7-6M42 20c-4 0-6 2-6 5M46 32c-4 0-7-2-8-5M38 42c0-4-3-6-7-6"/>
      </svg>
    </div>
    <p class="intro-text">Halverstead University researchers are seeking girls age 10-17 for a study about brain activity in emotions and decision-making and how they relate to puberty, anxiety and depression.</p>
  </div>

  <section class="card card-left">
    <div class="brain-sketch" role="img" aria-label="Line drawing of a brain"></div>
    <h2 class="card-heading">STUDY<br>PARTICIPATION<br>INVOLVES</h2>

    <div class="step" style="top:168px">
      <div class="step-icon copper">
        <svg width="36" height="36" viewBox="0 0 36 36" fill="none" stroke="#fff" stroke-width="1.8">
          <circle cx="18" cy="18" r="15"/><circle cx="18" cy="18" r="11"/><path d="M18 10v8l3 3"/>
        </svg>
      </div>
      <p class="step-text">One one-hour interview (online or in-person) where your child will discuss their thoughts</p>
    </div>

    <div class="step" style="top:259px">
      <div class="step-icon navy">
        <svg width="36" height="36" viewBox="0 0 36 36" fill="none" stroke="#fff" stroke-width="1.6">
          <rect x="5" y="4" width="14" height="18"/><path d="M8 8h8M8 12h8M8 16h8"/>
          <rect x="13" y="10" width="19" height="14"/><path d="M22 24v4M16 29h12"/>
        </svg>
      </div>
      <p class="step-text">Online questionnaires<br>(parent and child)</p>
    </div>

    <div class="step" style="top:336px">
      <div class="step-icon copper">
        <svg width="36" height="36" viewBox="0 0 36 36" fill="none" stroke="#fff" stroke-width="1.6">
          <rect x="5" y="5" width="20" height="25"/><path d="M9 10h3M15 10h3M21 10h0M9 15h3M15 15h3M9 20h3M15 20h3M12 30v-5h6v5"/>
          <path d="M28 22c-3 0-5 2-5 4 0 3 5 7 5 7s5-4 5-7c0-2-2-4-5-4z"/><circle cx="28" cy="26" r="1.3"/>
        </svg>
      </div>
      <p class="step-text">One two-hour visit where your child will complete an MRI scan, answer questions about their puberty stage, and have a small hair sample taken to study puberty hormones</p>
    </div>
  </section>

  <section class="card card-right">
    <h2 class="card-heading">YOUR CHILD MAY<br>BE ELIGIBLE IF THEY</h2>

    <div class="criteria" style="top:133px">
      <svg width="26" height="26" viewBox="0 0 26 26" fill="none" stroke="#c47a3a" stroke-width="1.8" stroke-linecap="round"><path d="M22 12a10 10 0 1 1-4-8"/><path d="M8 12l5 5 11-12"/></svg>
      <p>Are age 10-17</p>
    </div>
    <div class="criteria" style="top:176px">
      <svg width="26" height="26" viewBox="0 0 26 26" fill="none" stroke="#c47a3a" stroke-width="1.8" stroke-linecap="round"><path d="M22 12a10 10 0 1 1-4-8"/><path d="M8 12l5 5 11-12"/></svg>
      <p>Tend to worry or overthink negative thoughts</p>
    </div>
    <div class="criteria" style="top:242px">
      <svg width="26" height="26" viewBox="0 0 26 26" fill="none" stroke="#c47a3a" stroke-width="1.8" stroke-linecap="round"><path d="M22 12a10 10 0 1 1-4-8"/><path d="M8 12l5 5 11-12"/></svg>
      <p>Have not been diagnosed with psychosis, learning problems, or autism</p>
    </div>

    <div class="child-photo" role="img" aria-label="Glowing brain graphic beside a thoughtful teenage girl resting her chin on her hand"></div>
    <div class="compensation">
      <p class="label">Compensation</p>
      <p class="amount">Up to <strong>$140</strong></p>
    </div>
  </section>

  <footer class="footer">
    <p class="cta">Interested in participating? Want more information? Please <a>Contact us!</a></p>
    <p class="email">
      <svg width="17" height="17" viewBox="0 0 18 18" fill="none" stroke="#fff" stroke-width="1.5"><circle cx="9" cy="9" r="7.5"/><ellipse cx="9" cy="9" rx="3.2" ry="7.5"/><path d="M1.5 9h15M3 5h12M3 13h12"/></svg>
      molvtstudy@halverstead.edu
    </p>
    <span class="code">C9</span>
  </footer>
</div>
</body>
</html>
```